Leading In-Home Tutoring Company Needs Web Banners

We need a suite of web banners for our re-marketing campaign. We are based in Melbourne and heading into the busiest time of the year with back to school and we would like to help guide parents to working with us via quality designed banners with the right CTAs. Banner specs as follows (W x H in pixels)
Medium Rectangle: 300 x 250
Vertical rectangle: 240 x 400
Banner: 468 x 60
Leaderboard: 728 x 90
Square: 250 x 250
Mobile leaderboard: 320 x 50
Updates

Hi designers I'm new to this and didn't realise that I had to upload all files at the beginning. I have images that can be used for this project. Just need to work out how to upload them. Added Sunday, January 22, 2017

Hi awesome designers... I've updated the brief now with new files :)

Target Market(s)

Mothers who value kids education. Our customer can be found having morning coffee with friends in her lycra as she prepares to go to the gym. Middle class, inner city and suburban Mums. Most likely on Chatterloom.

Industry/Entity Type

It Company

Font styles to use
Sans Serif

Colors
0692cd
fbed22
f47f39
ec1f27

Requirements
Must have
• Wording should include.
• What we do: 1:1, In-Home Tutoring
• Value proposition: The Best Tutor For Your Child
• Call to Action - Free Assessment > Find Out More
• Adjusted layout to suit the sizes. Use of image where possible to provide immediate graphic display of what we do
Nice to have
• Keep it simple, create an emotive connection. Kids matter to parents and they will pay for services if we can create banners that show we care and can help wtih their education.
Should not have
• Anything negative or use fear marketing

```html
<!DOCTYPE html>
<html lang="en">
<head>
<meta charset="utf-8">
<title>Lumenwise Web Banner Suite</title>
<link rel="stylesheet" href="https://fonts.googleapis.com/css2?family=Arimo:wght@400;700&display=swap">
<style>
  :root {
    --blue: #0692cd;
    --blue-deep: #0a7fbf;
    --orange: #f47f39;
    --red: #ec1f27;
    --red-dark: #b8121a;
    --slate: #3d4b59;
    --slate-dark: #2f3b47;
    --ink: #4a5866;
    --white: #ffffff;
    --page: #ffffff;
    --frame: #8a8a8a;
    --photo-a: #8a98a8;
    --photo-b: #c9c2b4;
    --photo-c: #5a6f8e;
  }
  * { box-sizing: border-box; margin: 0; padding: 0; }
  html, body { width: 1200px; height: 1200px; overflow: hidden; background: var(--page); }
  body { font-family: "Arimo", Arial, sans-serif; }

  .suite {
    position: absolute; left: 0; top: 0;
    width: 850px; height: 850px;
    transform: scale(1.41176);
    transform-origin: 0 0;
  }
  .size-label {
    position: absolute; font-size: 16px; color: #111; letter-spacing: 0.2px;
  }

  .banner {
    position: absolute; overflow: hidden; background: var(--white);
    outline: 1px solid var(--frame);
  }
  .brand-area { position: absolute; background: var(--blue); }
  .brand {
    position: absolute; display: flex; align-items: center; gap: 4px;
    color: var(--white); font-weight: 700; white-space: nowrap;
  }
  .brand-dot { border-radius: 50%; background: var(--orange); flex: none; }

  .photo {
    position: absolute;
    background: linear-gradient(135deg, var(--photo-c) 0%, var(--photo-a) 40%, var(--photo-b) 75%, #e6e1d6 100%);
  }
  .red-rule { position: absolute; background: var(--red); }
  .blue-rule { position: absolute; background: var(--blue); }

  .value-panel {
    position: absolute;
    background: linear-gradient(180deg, var(--slate) 0%, var(--slate-dark) 100%);
  }
  .value-text {
    position: absolute; color: var(--white); font-weight: 700; text-align: center;
    text-shadow: 0 1px 2px rgba(0,0,0,.45); line-height: 1.05;
  }
  .ribbon {
    position: absolute; background: var(--orange); color: var(--white);
    font-weight: 700; text-align: center; line-height: 1.05;
    clip-path: polygon(0 0, 100% 0, 100% 100%, 50% 82%, 0 100%);
    text-shadow: 0 1px 1px rgba(0,0,0,.3);
    display: flex; justify-content: center; padding-top: 4px;
  }
  .swoosh { position: absolute; display: block; }

  .offer {
    position: absolute; color: var(--ink); font-weight: 700; line-height: 1.1;
  }
  .cta {
    position: absolute; display: flex; align-items: center; justify-content: space-between;
    background: linear-gradient(180deg, #ff4a4f 0%, var(--red) 55%, #d3141b 100%);
    border-radius: 3px; color: var(--white); font-weight: 700; white-space: nowrap;
    box-shadow: 0 1px 2px rgba(0,0,0,.35);
  }
  .cta-icon { flex: none; display: block; }
</style>
</head>
<body>
<main class="suite">

  <!-- Leaderboard 728 x 90 -->
  <section class="banner leaderboard" style="left:80px;top:39px;width:728px;height:90px;">
    <div class="brand-area" style="left:0;top:0;width:240px;height:90px;"></div>
    <div class="brand" style="left:12px;top:36px;font-size:21px;"><span class="brand-dot" style="width:10px;height:10px;"></span>Lumenwise</div>
    <div class="red-rule" style="left:238px;top:0;width:4px;height:90px;"></div>
    <div class="photo" role="img" aria-label="Tutor smiling beside a schoolboy at a desk with books" style="left:242px;top:0;width:160px;height:90px;"></div>
    <div class="blue-rule" style="left:402px;top:0;width:4px;height:90px;"></div>
    <div class="value-panel" style="left:406px;top:0;width:170px;height:90px;border-radius:0 90px 90px 0 / 0 45px 45px 0;box-shadow:4px 0 0 var(--orange);"></div>
    <div class="value-text" style="left:410px;top:6px;width:150px;font-size:18px;">The<br>Best Tutor<br>For Your<br>Child</div>
    <div class="ribbon" style="left:152px;top:0;width:122px;height:72px;font-size:17px;">1:1 In-Home<br>Tutoring</div>
    <div class="offer" style="left:586px;top:16px;font-size:14px;">FREE Assesment</div>
    <div class="cta" style="left:580px;top:46px;width:142px;height:35px;padding:0 5px 0 8px;font-size:14px;">Find Out More
      <svg class="cta-icon" width="27" height="27" viewBox="0 0 27 27"><circle cx="13.5" cy="13.5" r="13" fill="#5a0a0e"/><path d="M10 7.5 L19.5 13.5 L10 19.5 Z" fill="#fff"/></svg>
    </div>
  </section>
  <div class="size-label" style="left:157px;top:140px;">728X90</div>

  <!-- Mobile leaderboard 320 x 50 -->
  <section class="banner mobile-leaderboard" style="left:448px;top:176px;width:320px;height:50px;">
    <div class="brand-area" style="left:0;top:0;width:95px;height:50px;"></div>
    <div class="brand" style="left:8px;top:8px;font-size:11px;gap:2px;"><span class="brand-dot" style="width:6px;height:6px;"></span>Lumenwise</div>
    <div style="position:absolute;left:0;top:30px;width:95px;height:20px;background:var(--orange);color:#fff;font-weight:700;font-size:8.5px;text-align:center;line-height:20px;">1:1 In-HomeTutoring</div>
    <div class="red-rule" style="left:94px;top:0;width:3px;height:50px;"></div>
    <div class="photo" role="img" aria-label="Tutor and schoolboy working together at a desk" style="left:97px;top:0;width:60px;height:50px;"></div>
    <div class="value-panel" style="left:157px;top:0;width:76px;height:50px;border-radius:0 40px 40px 0 / 0 25px 25px 0;box-shadow:3px 0 0 var(--orange);"></div>
    <div class="value-text" style="left:158px;top:2px;width:68px;font-size:10px;">The<br>Best Tutor<br>For Your<br>Child</div>
    <div class="offer" style="left:242px;top:8px;font-size:8px;">FREE Assesment</div>
    <div class="cta" style="left:237px;top:25px;width:78px;height:19px;padding:0 2px 0 5px;font-size:8px;">Find Out More
      <svg class="cta-icon" width="15" height="15" viewBox="0 0 27 27"><circle cx="13.5" cy="13.5" r="13" fill="#5a0a0e"/><path d="M10 7.5 L19.5 13.5 L10 19.5 Z" fill="#fff"/></svg>
    </div>
  </section>
  <div class="size-label" style="left:565px;top:235px;">320X50</div>

  <!-- Vertical rectangle 240 x 400 -->
  <section class="banner vertical-rectangle" style="left:85px;top:198px;width:240px;height:400px;">
    <div class="brand-area" style="left:0;top:0;width:240px;height:62px;"></div>
    <div class="brand" style="left:52px;top:30px;font-size:21px;"><span class="brand-dot" style="width:10px;height:10px;"></span>Lumenwise</div>
    <div class="red-rule" style="left:0;top:62px;width:240px;height:4px;"></div>
    <div class="photo" role="img" aria-label="Tutor and schoolboy talking at a desk in front of bookshelves" style="left:0;top:66px;width:240px;height:160px;"></div>
    <div class="blue-rule" style="left:0;top:212px;width:240px;height:4px;"></div>
    <div class="value-panel" style="left:0;top:216px;width:240px;height:135px;"></div>
    <svg class="swoosh" style="left:0;top:318px;" width="240" height="40" viewBox="0 0 240 40" preserveAspectRatio="none"><path d="M0 34 Q120 0 240 14 L240 40 L0 40 Z" fill="#fff"/><path d="M0 34 Q120 0 240 14" stroke="#f47f39" stroke-width="5" fill="none"/></svg>
    <div class="ribbon" style="left:51px;top:172px;width:138px;height:70px;font-size:19px;padding-top:8px;">1:1 In-Home<br>Tutoring</div>
    <div class="value-text" style="left:10px;top:261px;width:220px;font-size:22px;line-height:1.1;">The Best Tutor<br>For Your<br>Child</div>
    <div class="offer" style="left:6px;top:356px;font-size:14px;">FREE<br>Assesment</div>
    <div class="cta" style="left:92px;top:358px;width:141px;height:35px;padding:0 5px 0 6px;font-size:14px;">Find Out More
      <svg class="cta-icon" width="27" height="27" viewBox="0 0 27 27"><circle cx="13.5" cy="13.5" r="13" fill="#5a0a0e"/><path d="M10 7.5 L19.5 13.5 L10 19.5 Z" fill="#fff"/></svg>
    </div>
  </section>
  <div class="size-label" style="left:152px;top:611px;">240X400</div>

  <!-- Square 250 x 250 -->
  <section class="banner square" style="left:447px;top:270px;width:250px;height:250px;">
    <div class="brand-area" style="left:0;top:0;width:250px;height:64px;"></div>
    <div class="brand" style="left:6px;top:32px;font-size:17px;"><span class="brand-dot" style="width:8px;height:8px;"></span>Lumenwise</div>
    <div class="red-rule" style="left:0;top:64px;width:250px;height:3px;"></div>
    <div class="photo" role="img" aria-label="Tutor and schoolboy at a desk with books" style="left:0;top:67px;width:118px;height:125px;"></div>
    <div class="blue-rule" style="left:118px;top:60px;width:5px;height:132px;"></div>
    <div class="value-panel" style="left:123px;top:60px;width:127px;height:132px;"></div>
    <svg class="swoosh" style="left:0;top:170px;" width="250" height="32" viewBox="0 0 250 32" preserveAspectRatio="none"><path d="M0 26 Q125 -2 250 12 L250 32 L0 32 Z" fill="#fff"/><path d="M0 26 Q125 -2 250 12" stroke="#f47f39" stroke-width="4" fill="none"/></svg>
    <div class="ribbon" style="left:130px;top:16px;width:112px;height:68px;font-size:16px;">1:1 In-Home<br>Tutoring</div>
    <div class="value-text" style="left:124px;top:80px;width:124px;font-size:19px;line-height:1.1;">The<br>Best Tutor<br>For Your<br>Child</div>
    <div class="offer" style="left:10px;top:207px;font-size:13px;">FREE<br>Assesment</div>
    <div class="cta" style="left:100px;top:207px;width:142px;height:35px;padding:0 5px 0 6px;font-size:14px;">Find Out More
      <svg class="cta-icon" width="27" height="27" viewBox="0 0 27 27"><circle cx="13.5" cy="13.5" r="13" fill="#5a0a0e"/><path d="M10 7.5 L19.5 13.5 L10 19.5 Z" fill="#fff"/></svg>
    </div>
  </section>
  <div class="size-label" style="left:530px;top:523px;">250X250</div>

  <!-- Medium rectangle 300 x 250 -->
  <section class="banner medium-rectangle" style="left:449px;top:548px;width:300px;height:250px;">
    <div class="brand-area" style="left:0;top:0;width:300px;height:64px;"></div>
    <div class="brand" style="left:12px;top:36px;font-size:20px;"><span class="brand-dot" style="width:9px;height:9px;"></span>Lumenwise</div>
    <div class="red-rule" style="left:0;top:64px;width:300px;height:3px;"></div>
    <div class="photo" role="img" aria-label="Tutor and schoolboy at a desk with books" style="left:0;top:67px;width:146px;height:125px;"></div>
    <div class="blue-rule" style="left:146px;top:60px;width:5px;height:132px;"></div>
    <div class="value-panel" style="left:151px;top:60px;width:149px;height:132px;"></div>
    <svg class="swoosh" style="left:0;top:170px;" width="300" height="32" viewBox="0 0 300 32" preserveAspectRatio="none"><path d="M0 26 Q150 -2 300 12 L300 32 L0 32 Z" fill="#fff"/><path d="M0 26 Q150 -2 300 12" stroke="#f47f39" stroke-width="4" fill="none"/></svg>
    <div class="ribbon" style="left:156px;top:12px;width:136px;height:80px;font-size:19px;padding-top:7px;">1:1 In-Home<br>Tutoring</div>
    <div class="value-text" style="left:152px;top:90px;width:146px;font-size:19px;line-height:1.12;">The<br>Best Tutor<br>For Your<br>Child</div>
    <div class="offer" style="left:16px;top:219px;font-size:14px;">FREE Assesment</div>
    <div class="cta" style="left:150px;top:209px;width:141px;height:35px;padding:0 5px 0 6px;font-size:14px;">Find Out More
      <svg class="cta-icon" width="27" height="27" viewBox="0 0 27 27"><circle cx="13.5" cy="13.5" r="13" fill="#5a0a0e"/><path d="M10 7.5 L19.5 13.5 L10 19.5 Z" fill="#fff"/></svg>
    </div>
  </section>
  <div class="size-label" style="left:572px;top:809px;">300X250</div>

</main>
</body>
</html>
```